Organic skincare label - minimalist, earthy, luxe design needed!

I need a label design for a luxury natural skin care line called "Velka Botanix". Velka means 'earth' in Swahili. I would like the design to embody an earthy feel but be minimalistic and give a luxe vibe. My first product will be a Tumeric and Neem Scrub.

The size of the jar is 8oz, label dimensions should be (1.625" Tall x 8.5" Wide)
I will be making other products too such as; oils + toners so I feel free to do labels for glass bottles and/or spray bottles as well.

Forest green, light pinks/nudes/beige, grey, white, gold, are colors that can be used (not all have to be used).

I have included pictures of some things I've worked on myself as well as my original logo design but I need to simplify the logo, no circle around it.
Feel free to get creative.

Thank you! :)
Updates

Target Market(s)

Socially Conscious, Beauty Enthusiast, Minimalist

Industry/Entity Type

Skin Care

Font styles to use
Sans Serif
Other font styles liked:
• "Wonderlove doodle" is the font used for "Velka" in the logo. Feel free to use that or change it as you see fit.

Requirements
Must have
• Simplistic design
would like to stick to a font close to the ones in the logo. Either the one used for the name "Velka" OR the one that the slogan "rooted rituals" uses.

I have also included some pictures to capture the aesthetic of my social media and website.

Gender neutral

```html
<!DOCTYPE html>
<html lang="en">
<head>
<meta charset="utf-8">
<title>Velka Botanix — Label Variants</title>
<link href="https://fonts.googleapis.com/css2?family=Jost:wght@300;400&display=swap" rel="stylesheet">
<style>
  :root {
    --paper: #ffffff;
    --ink: #141414;
    --coral: #ec6f66;
    --sand: #d6cdb9;
  }
  * { margin: 0; padding: 0; box-sizing: border-box; }
  html, body {
    width: 1200px;
    height: 600px;
    overflow: hidden;
    background: var(--paper);
  }
  .sheet {
    position: relative;
    width: 1200px;
    height: 600px;
    font-family: 'Jost', 'Century Gothic', sans-serif;
    color: var(--ink);
  }
  .label {
    position: absolute;
    top: 0;
    width: 300px;
    height: 600px;
    text-align: center;
  }
  .label--one   { left: -4px; }
  .label--two   { left: 306px; }
  .label--three { left: 614px; top: 6px; }
  .label--four  { left: 924px; top: 6px; }
  .label--compact .brand { top: 192px; }

  .brand {
    position: absolute;
    left: 0;
    right: 0;
    top: 158px;
    display: flex;
    justify-content: center;
    align-items: center;
    gap: 8px;
    height: 38px;
  }
  .brand__name {
    font-weight: 400;
    font-size: 32px;
    letter-spacing: 0.04em;
    line-height: 1;
  }
  .brand__dot {
    width: 10px;
    height: 10px;
    border-radius: 50%;
    margin-top: 10px;
  }
  .brand--ink .brand__name { color: var(--ink); }
  .brand--coral .brand__name { color: var(--coral); }
  .brand__dot--coral { background: var(--coral); }
  .brand__dot--sand { background: var(--sand); }

  .tagline {
    position: absolute;
    left: 0; right: 0;
    top: 252px;
    font-weight: 300;
    font-size: 18px;
    line-height: 21px;
    letter-spacing: 0.17em;
  }
  .rule {
    position: absolute;
    left: 129px;
    width: 43px;
    height: 1px;
    background: var(--ink);
  }
  .rule--upper { top: 311px; }
  .rule--lower { top: 421px; }
  .ingredients {
    position: absolute;
    left: 0; right: 0;
    top: 328px;
    font-weight: 300;
    font-size: 13px;
    line-height: 14.8px;
    letter-spacing: 0.15em;
    list-style: none;
  }
  .origin {
    position: absolute;
    left: 0; right: 0;
    top: 443px;
    font-weight: 300;
    font-size: 12.5px;
    letter-spacing: 0.15em;
  }
</style>
</head>
<body>
<main class="sheet">

  <section class="label label--one">
    <div class="brand brand--ink"><span class="brand__name">Velka</span><span class="brand__dot brand__dot--coral"></span></div>
    <p class="tagline">rooted rituals<br>organic skincare</p>
    <div class="rule rule--upper"></div>
    <ul class="ingredients">
      <li>Ingredients:</li>
      <li>Organic Rosehip Seed Oil</li>
      <li>Organic Camellia Seed Oil</li>
      <li>Organic Pomegranete Oil</li>
      <li>VitamineE Non-GMO</li>
    </ul>
    <div class="rule rule--lower"></div>
    <p class="origin">Made in Cedar Vale, TX</p>
  </section>

  <section class="label label--two">
    <div class="brand brand--coral"><span class="brand__name">Velka</span><span class="brand__dot brand__dot--sand"></span></div>
    <p class="tagline">rooted rituals<br>organic skincare</p>
    <div class="rule rule--upper"></div>
    <ul class="ingredients">
      <li>Ingredients:</li>
      <li>Organic Rosehip Seed Oil</li>
      <li>Organic Camellia Seed Oil</li>
      <li>Organic Pomegranete Oil</li>
      <li>VitamineE Non-GMO</li>
    </ul>
    <div class="rule rule--lower"></div>
    <p class="origin">Made in Cedar Vale, TX</p>
  </section>

  <section class="label label--three label--compact">
    <div class="brand brand--ink"><span class="brand__name">Velka</span><span class="brand__dot brand__dot--sand"></span></div>
    <p class="tagline">rooted rituals<br>organic skincare</p>
    <div class="rule rule--upper"></div>
    <ul class="ingredients">
      <li>Ingredients:</li>
      <li>Organic Rosehip Seed Oil</li>
      <li>Organic Camellia Seed Oil</li>
      <li>Organic Pomegranete Oil</li>
      <li>VitamineE Non-GMO</li>
    </ul>
    <div class="rule rule--lower"></div>
    <p class="origin">Made in Cedar Vale, TX</p>
  </section>

  <section class="label label--four label--compact">
    <div class="brand brand--coral"><span class="brand__name">Velka</span><span class="brand__dot brand__dot--coral"></span></div>
    <p class="tagline">rooted rituals<br>organic skincare</p>
    <div class="rule rule--upper"></div>
    <ul class="ingredients">
      <li>Ingredients:</li>
      <li>Organic Rosehip Seed Oil</li>
      <li>Organic Camellia Seed Oil</li>
      <li>Organic Pomegranete Oil</li>
      <li>VitamineE Non-GMO</li>
    </ul>
    <div class="rule rule--lower"></div>
    <p class="origin">Made in Cedar Vale, TX</p>
  </section>

</main>
</body>
</html>
```